Property investor needs a business card with logo

I need a business card for a UK based business called 'Bright Door Homes'. I buy houses quickly that is either hard to sell or people have been having trouble to sell. I then create the opportunity for people to buy houses that normally can't. This could be because they have little or no deposit saved up or they don't qualify for a mortgage. The design is to be bright so that it stands out but non threatening and basic. Yellow for the bass colour. The logo to be very simple and represent a house. It could include words like "cant sell? I'll buy it!!" or "Need a quick sale? Let me help" or something as simple as "I buy houses!!" The final design should communicate that I am not some big corporate person that is better that them, but someone that is just a person trying to help them with their situation. with a picture of me with the background removed.
Target Market(s)
Normal everyday people
Industry/Entity Type
Business
Contact Information for Business Card
Derek Pallister
07845619027
brightdoorhomes@mailbox.example
Font styles to use
Other font styles liked:
- something that looks hand written
Look and feel

```html
<!DOCTYPE html>
<html lang="en">
<head>
<meta charset="utf-8">
<title>Bright Door Homes – Business Card</title>
<link rel="stylesheet" href="https://fonts.googleapis.com/css2?family=Cormorant+Upright:wght@500&family=Open+Sans:wght@400&family=Indie+Flower&display=swap">
<style>
  :root {
    --backdrop: #e9e4dc;
    --card-black: #2a2828;
    --brand-yellow: #f7e81e;
    --stripe-white: #ffffff;
    --text-white: #ffffff;
    --photo-dark: #2b3442;
    --photo-light: #8c8f96;
  }
  * { margin: 0; padding: 0; box-sizing: border-box; }
  html, body { width: 1083px; height: 1200px; overflow: hidden; }
  body { background: var(--backdrop); position: relative; }

  .card {
    position: absolute;
    width: 840px;
    height: 479px;
    background: var(--card-black);
    overflow: hidden;
  }
  .card--front { left: 107px; top: 82px; }
  .card--back { left: 117px; top: 626px; }

  .card__waves { position: absolute; inset: 0; width: 840px; height: 479px; }

  .card__photo {
    position: absolute;
    left: 440px;
    top: 112px;
    width: 400px;
    height: 367px;
    background: linear-gradient(180deg, var(--photo-light) 0%, var(--photo-dark) 70%);
    border-radius: 180px 180px 0 0;
  }

  .brand {
    position: absolute;
    display: flex;
    align-items: center;
  }
  .brand__mark {
    flex: none;
    background: var(--brand-yellow);
  }
  .brand__name {
    font-family: "Cormorant Upright", serif;
    font-weight: 500;
    color: var(--text-white);
    white-space: nowrap;
    text-align: center;
  }
  .brand__line { display: block; }

  .card--front .brand { left: 48px; top: 72px; gap: 22px; }
  .card--front .brand__mark { width: 30px; height: 30px; }
  .card--front .brand__name { font-size: 44px; line-height: 64px; }

  .card--back .brand { left: 0; right: 0; top: 128px; justify-content: center; gap: 34px; }
  .card--back .brand__mark { width: 42px; height: 42px; }
  .card--back .brand__name { font-size: 60px; line-height: 96px; }

  .holder-name {
    position: absolute;
    left: 480px;
    top: 38px;
    width: 320px;
    text-align: center;
    font-family: "Cormorant Upright", serif;
    font-weight: 500;
    font-size: 34px;
    color: var(--text-white);
  }

  .contact {
    position: absolute;
    left: 40px;
    top: 252px;
    list-style: none;
    font-family: "Open Sans", sans-serif;
    font-size: 17px;
    color: var(--text-white);
  }
  .contact__item { display: flex; align-items: center; height: 30px; margin-bottom: 16px; }
  .contact__icon { width: 15px; height: 15px; margin-right: 11px; fill: var(--text-white); }

  .tagline {
    position: absolute;
    left: 0;
    right: 0;
    top: 398px;
    text-align: center;
    font-family: "Indie Flower", cursive;
    font-size: 46px;
    line-height: 52px;
    color: var(--brand-yellow);
  }
</style>
</head>
<body>

  <section class="card card--front">
    <svg class="card__waves" viewBox="0 0 840 479" aria-hidden="true">
      <path d="M0,405 C160,392 300,350 378,330 C300,372 160,410 0,420 Z" fill="var(--brand-yellow)"/>
      <path d="M0,428 C200,415 390,330 510,255 C620,190 730,205 840,192 L840,214 C730,226 630,215 520,275 C400,350 210,440 0,452 Z" fill="var(--stripe-white)"/>
      <path d="M0,455 C210,445 400,355 525,282 C630,222 735,232 840,218 L840,479 L0,479 Z" fill="var(--brand-yellow)"/>
    </svg>
    <div class="card__photo" role="img" aria-label="Portrait photo of Derek Pallister with background removed"></div>
    <div class="brand">
      <span class="brand__mark" aria-hidden="true"></span>
      <p class="brand__name"><span class="brand__line">Bright</span><span class="brand__line">Door Homes</span></p>
    </div>
    <p class="holder-name">Derek Pallister</p>
    <ul class="contact">
      <li class="contact__item">
        <svg class="contact__icon" viewBox="0 0 16 16" aria-hidden="true"><path d="M4 1 L6 1 L7 5 L5.5 6.5 C6.5 8.5 7.5 9.5 9.5 10.5 L11 9 L15 10 L15 12 C15 14 13 15 11.5 15 C6 14 2 10 1 4.5 C1 3 2 1 4 1 Z"/></svg>
        <span>07845619027</span>
      </li>
      <li class="contact__item">
        <svg class="contact__icon" viewBox="0 0 16 16" aria-hidden="true"><path d="M1 4 L8 9 L15 4 L15 14 L1 14 Z M1 2.5 L15 2.5 L8 7.5 Z"/></svg>
        <span>brightdoorhomes@mailbox.example</span>
      </li>
    </ul>
  </section>

  <section class="card card--back">
    <div class="brand">
      <span class="brand__mark" aria-hidden="true"></span>
      <p class="brand__name"><span class="brand__line">Bright</span><span class="brand__line">Door Homes</span></p>
    </div>
    <p class="tagline">cant sell? I'll buy it!!</p>
  </section>

</body>
</html>
```